Thermostat Screen Design

We need a screen layout design for a new thermostat we're currently developing. If you're not familiar with thermostats, you can see some examples here - http://heating-dials-compared.bestlistguide.example/

We're after the main page design, with icons, colours etc. It needs to be clean, modern and minimalistic. Attached is all components required on the screen. The screen size is 5 inch (diagnol).

The arrows on the screen showcase what happens when you press a button. For example, when you press MODE once you get OFF, press it twice, HEAT, press it 3 times, COOL, etc. This is just for your reference.

You have complete creative license on how you choose to layout the screen, position the components etc, but we require:

- it must be on a 5 inch screen diagnol
- modern, clean and minimalistic
- includes icons and colours
- Intuitive

Let me know if any questions.

```html
<!DOCTYPE html>
<html lang="en">
<head>
<meta charset="utf-8">
<title>Thermostat Main Screen</title>
<link rel="stylesheet" href="https://fonts.googleapis.com/css2?family=Electrolize&display=swap">
<style>
  :root {
    --bg: #000000;
    --orange: #ff8a00;
    --orange-soft: #f7a02a;
    --orange-text: #d98a2a;
    --blue: #0d6bff;
    --blue-light: #4a8cff;
    --blue-text: #5b8ef5;
    --blue-deep: #1663e8;
    --white: #ffffff;
  }
  * { box-sizing: border-box; margin: 0; padding: 0; }
  html, body {
    width: 1200px; height: 960px; overflow: hidden;
    background: var(--bg);
    font-family: "Electrolize", sans-serif;
  }
  .screen {
    position: relative;
    width: 1181px; height: 945px;
    transform: scale(1.0161, 1.0159);
    transform-origin: 0 0;
  }
  .abs { position: absolute; line-height: 1; white-space: nowrap; }
  .date {
    left: 232px; top: 44px;
    font-size: 38px; letter-spacing: 3px;
    color: var(--blue-text);
  }
  .pill {
    display: flex; align-items: center; justify-content: center;
    border-radius: 8px; color: var(--white);
    text-transform: uppercase;
  }
  .pill--orange { background: var(--orange); }
  .pill--blue { background: var(--blue); }
  .pill--light { background: var(--blue-light); }
  .status-sleep { left: 836px; top: 21px; width: 124px; height: 45px; font-size: 20px; }
  .status-zone { left: 990px; top: 21px; width: 124px; height: 45px; font-size: 20px; }
  .clock { left: 866px; top: 112px; }
  .side-btn { left: 29px; width: 90px; height: 90px; font-size: 15px; }
  .side-btn--mode { top: 250px; }
  .side-btn--fan { top: 369px; }
  .side-btn--settings { top: 488px; font-size: 13px; }
  .side-btn--zones { top: 606px; }
  .reading-label { font-size: 16px; color: var(--orange); letter-spacing: 0.5px; top: 236px; }
  .reading-label--outdoor { left: 234px; }
  .reading-label--rh { left: 420px; }
  .outdoor-dial { left: 226px; top: 267px; }
  .reading-value { font-size: 40px; color: var(--orange-text); top: 286px; }
  .reading-value--outdoor { left: 288px; }
  .reading-value--rh { left: 433px; }
  .deg-small {
    position: absolute; left: 333px; top: 277px;
    width: 6px; height: 6px; border-radius: 50%; background: var(--orange-text);
  }
  .room-ring { left: 226px; top: 363px; }
  .room-value {
    left: 331px; top: 480px;
    font-size: 80px; color: var(--blue-deep);
  }
  .room-deg {
    left: 424px; top: 475px; width: 14px; height: 14px;
    border-radius: 50%; background: var(--blue);
  }
  .room-label { left: 289px; top: 615px; font-size: 38px; letter-spacing: 2px; color: var(--blue); }
  .setpoint-label { left: 575px; font-size: 25px; color: var(--blue-text); letter-spacing: 0.5px; }
  .setpoint-label--heat { top: 443px; }
  .setpoint-label--cool { top: 543px; }
  .setpoint-btn { left: 794px; }
  .setpoint-btn--up { top: 425px; }
  .setpoint-btn--down { top: 526px; }
  .legend { top: 849px; height: 42px; font-size: 14px; letter-spacing: 0.5px; }
  .legend--mode { left: 70px; width: 251px; }
  .legend--fan { left: 346px; width: 191px; }
  .legend--icons { left: 561px; width: 225px; }
  .legend--zones { left: 811px; width: 291px; }
</style>
</head>
<body>
<main class="screen">
  <div class="abs date">WED JULY 2014</div>

  <div class="abs pill pill--orange status-sleep">Sleep</div>
  <div class="abs pill pill--blue status-zone">Zone 1</div>

  <svg class="abs clock" width="222" height="222" viewBox="0 0 222 222" aria-label="Analog clock">
    <circle cx="111" cy="110" r="108" fill="none" stroke="var(--orange-soft)" stroke-width="3"/>
    <g stroke="var(--orange-soft)" stroke-width="4">
      <line x1="111" y1="17" x2="111" y2="28"/>
      <line x1="111" y1="192" x2="111" y2="203"/>
      <line x1="18" y1="110" x2="29" y2="110"/>
      <line x1="193" y1="110" x2="204" y2="110"/>
      <g transform="rotate(30 111 110)"><line x1="111" y1="21" x2="111" y2="30"/></g>
      <g transform="rotate(60 111 110)"><line x1="111" y1="21" x2="111" y2="30"/></g>
      <g transform="rotate(120 111 110)"><line x1="111" y1="21" x2="111" y2="30"/></g>
      <g transform="rotate(150 111 110)"><line x1="111" y1="21" x2="111" y2="30"/></g>
      <g transform="rotate(210 111 110)"><line x1="111" y1="21" x2="111" y2="30"/></g>
      <g transform="rotate(240 111 110)"><line x1="111" y1="21" x2="111" y2="30"/></g>
      <g transform="rotate(300 111 110)"><line x1="111" y1="21" x2="111" y2="30"/></g>
      <g transform="rotate(330 111 110)"><line x1="111" y1="21" x2="111" y2="30"/></g>
    </g>
    <line x1="111" y1="128" x2="111" y2="51" stroke="var(--orange-soft)" stroke-width="5"/>
    <line x1="111" y1="110" x2="174" y2="146" stroke="var(--orange-soft)" stroke-width="3"/>
    <line x1="111" y1="110" x2="87" y2="96" stroke="var(--orange-soft)" stroke-width="3"/>
    <circle cx="111" cy="110" r="5" fill="var(--orange-soft)"/>
  </svg>

  <div class="abs pill pill--orange side-btn side-btn--mode">Mode</div>
  <div class="abs pill pill--blue side-btn side-btn--fan">Fan</div>
  <div class="abs pill pill--orange side-btn side-btn--settings">Settings</div>
  <div class="abs pill pill--blue side-btn side-btn--zones">Zones</div>

  <div class="abs reading-label reading-label--outdoor">OUTDOOR TEM</div>
  <div class="abs reading-label reading-label--rh">INDOOR RH</div>

  <svg class="abs outdoor-dial" width="80" height="80" viewBox="0 0 80 80" aria-hidden="true">
    <path d="M58 10 A32 32 0 1 0 58 70" fill="none" stroke="var(--orange)" stroke-width="9"/>
  </svg>
  <div class="abs reading-value reading-value--outdoor">30</div>
  <span class="deg-small"></span>
  <div class="abs reading-value reading-value--rh">45%</div>

  <svg class="abs room-ring" width="310" height="250" viewBox="0 0 310 250" aria-hidden="true">
    <defs>
      <linearGradient id="ring-fade" x1="0" y1="0" x2="0" y2="1">
        <stop offset="0" stop-color="#0d6bff"/>
        <stop offset="0.6" stop-color="#4a8cff"/>
        <stop offset="0.8" stop-color="#2e6fe0"/>
        <stop offset="0.97" stop-color="#000000" stop-opacity="1"/>
      </linearGradient>
    </defs>
    <circle cx="155" cy="155" r="134" fill="none" stroke="url(#ring-fade)" stroke-width="38"/>
  </svg>
  <div class="abs room-value">30</div>
  <span class="abs room-deg"></span>
  <div class="abs room-label">ROOM TEM</div>

  <div class="abs setpoint-label setpoint-label--heat">HEAT SET POINT</div>
  <svg class="abs setpoint-btn setpoint-btn--up" width="60" height="60" viewBox="0 0 60 60" aria-label="Raise heat set point">
    <circle cx="30" cy="30" r="28" fill="none" stroke="var(--blue)" stroke-width="2.5"/>
    <polygon points="30,9 11,43 30,35 49,43" fill="var(--blue-light)"/>
  </svg>
  <div class="abs setpoint-label setpoint-label--cool">COOL SET POINT</div>
  <svg class="abs setpoint-btn setpoint-btn--down" width="60" height="60" viewBox="0 0 60 60" aria-label="Lower cool set point">
    <circle cx="30" cy="30" r="28" fill="none" stroke="var(--blue)" stroke-width="2.5"/>
    <polygon points="30,51 11,17 30,25 49,17" fill="var(--blue-light)"/>
  </svg>

  <div class="abs pill pill--orange legend legend--mode">OFF HEAT &nbsp;COOL AUTO</div>
  <div class="abs pill pill--orange legend legend--fan">FAN ICONS: AUTO</div>
  <div class="abs pill pill--light legend legend--icons">MODE ICONS: HEAT COOL</div>
  <div class="abs pill pill--light legend legend--zones">ZONE 1 &nbsp;ZONE 2 &nbsp;ZONE 3 &nbsp;ZONE 4</div>
</main>
</body>
</html>
```